Homepage design for female-owned English/French speaking Law firm

Brief Update - we prefer not to have a photo of a person in the hero shot

Morlewy.com.au is the website for a English/French Bilingual Female-owned Law Firm, Quillomette Morlewy.
Overall Design notes:
Professional, yet warm and welcoming
Historic foundations but Progressive, woman-owned, sleek, innovative and modern.
Approachable, casual yet professional. Sans-serif font and light colours would help this
2 languages switched by flags (English/French)

Winner must provide
Home page design
Standard (inner) page design (can be provided after winner is selected)
All photos used in the design without charge

Number of Pages Required

2 page

Requirements
Should not have
• Update - we prefer not to have a photo of a person in the hero shot

```html
<!DOCTYPE html>
<html lang="en">
<head>
<meta charset="utf-8">
<title>Quillomette Morlewy</title>
<link href="https://fonts.googleapis.com/css2?family=Inter:wght@400;500;600;700;800&display=swap" rel="stylesheet">
<style>
:root{
  --orange:#f46a1f;
  --ink:#1d1d1f;
  --text:#4b4f58;
  --muted:#8a8f98;
  --band:#f2f3f5;
  --card:#f6f6f7;
  --line:#d9dbe0;
  --white:#ffffff;
}
*{box-sizing:border-box;margin:0;padding:0}
html,body{width:1200px;height:5085px;overflow:hidden}
body{font-family:"Inter",sans-serif;color:var(--ink);background:var(--white);position:relative}
section,header,footer{position:absolute;left:0;width:1200px}
.abs{position:absolute}
.btn{position:absolute;background:var(--orange);color:#fff;border-radius:22px;font-size:12px;font-weight:600;display:flex;align-items:center;justify-content:center}
.label{color:var(--orange);font-size:13px}
.arrow-btn{position:absolute;width:30px;height:30px;border-radius:50%;display:flex;align-items:center;justify-content:center}
.arrow-btn.on{background:var(--orange)}
.arrow-btn.off{background:#fff;border:1px solid var(--line)}
.dots{position:absolute;display:flex;gap:14px}
.dots i{width:7px;height:7px;border-radius:50%;background:#d0d2d6;display:block}
.dots i:first-child{background:var(--orange)}

/* header */
.site-header{top:0;height:50px;background:#fff}
.brand{position:absolute;left:136px;top:15px;display:flex;align-items:center;gap:9px;font-size:15px;font-weight:600;color:var(--ink)}
.brand i{width:14px;height:14px;background:var(--orange);display:block}
.nav{position:absolute;left:459px;top:18px;display:flex;gap:22px;font-size:11px}
.phone-btn{left:903px;top:10px;width:141px;height:28px;font-size:11px}

/* hero */
.hero{top:50px;height:544px}
.hero-photo{position:absolute;inset:0;background:linear-gradient(180deg,#5f7fd3 0%,#9aaee6 35%,#d6a6b8 55%,#3a5590 72%,#1c2f6a 100%)}
.hero-card{position:absolute;left:120px;top:128px;width:462px;height:272px;background:rgba(235,238,248,.7);border-radius:6px;padding:44px 36px}
.hero-card h1{font-size:32px;line-height:41px;font-weight:600;letter-spacing:-.4px}
.hero-card h1 strong{font-weight:700}
.hero-card p{font-size:12px;color:var(--text);margin-top:12px}
.hero-card .btn{left:36px;top:185px;width:218px;height:42px}

/* trust band */
.trust{top:594px;height:284px;background:var(--band)}
.trust h2{position:absolute;left:156px;top:66px;font-size:21px;font-weight:600}
.trust p{position:absolute;left:156px;top:112px;width:460px;font-size:11.5px;line-height:20px;color:var(--text)}
.win{position:absolute;right:156px;top:64px;text-align:right}
.win span{display:block;font-size:33px;font-weight:600}
.win strong{display:block;font-size:90px;font-weight:800;color:var(--orange);line-height:82px;letter-spacing:-1px}

/* reasons */
.reasons{top:878px;height:548px}
.sec-title{position:absolute;left:0;width:1200px;text-align:center;font-size:45px;font-weight:600;letter-spacing:-.5px}
.reasons .sec-title{top:88px}
.reason{position:absolute;top:184px;width:280px;height:288px;background:var(--card);border-radius:14px;padding:52px 32px}
.reason h3{font-size:15px;font-weight:600;margin-top:26px}
.reason p{font-size:11.5px;line-height:21px;color:var(--text);margin-top:14px}
.reason .go{margin-top:14px}

/* serve */
.serve{top:1426px;height:344px}
.serve-photo{position:absolute;left:156px;top:0;width:456px;height:344px;background:linear-gradient(180deg,#bfc3c9,#6d7079 60%,#2e3038)}
.serve-panel{position:absolute;left:612px;top:0;width:430px;height:344px;background:var(--band);padding:62px 54px}
.serve-panel h2{font-size:26px;font-weight:600;line-height:33px}
.serve-panel p{font-size:11.5px;line-height:21px;color:var(--text);margin-top:22px}
.serve-panel .btn{left:54px;top:232px;width:218px;height:44px}

/* awards */
.awards{top:1770px;height:420px}
.awards .sec-title{top:86px}
.badge{position:absolute;top:188px;width:96px;height:96px;border-radius:50%;background:#e7e9ee;border:3px solid #c8ccd4}
.badge.sq{border-radius:4px;width:60px;height:84px;top:194px}

/* cases */
.cases{top:2190px;height:778px;background:var(--band);overflow:hidden}
.cases .label{position:absolute;left:158px;top:88px}
.cases h2{position:absolute;left:156px;top:126px;width:500px;font-size:44px;line-height:55px;font-weight:700;letter-spacing:-.5px}
.cases .intro{position:absolute;left:690px;top:82px;width:360px;font-size:11.5px;line-height:21px;color:var(--text)}
.case{position:absolute;top:332px;width:206px}
.case .ph{height:263px}
.case h4{text-align:center;font-size:15px;font-weight:500;margin-top:16px;color:var(--text)}
.case.active h4{color:var(--orange);font-weight:600}
.track{position:absolute;left:156px;top:687px;width:768px;height:2px;background:#d7d9de}
.track i{position:absolute;left:0;top:-1px;width:280px;height:4px;background:var(--orange)}

/* testimonials */
.testimonials{top:2968px;height:637px}
.testimonials .sec-title{top:86px;line-height:55px}
.quote{position:absolute;top:252px;width:282px;height:230px;background:#fff;border-radius:12px;box-shadow:0 6px 22px rgba(0,0,0,.09);padding:34px 32px}
.quote .qmark{position:absolute;right:28px;top:-12px;width:26px;height:26px;border-radius:50%;background:var(--orange);color:#fff;font-size:16px;font-weight:700;text-align:center;line-height:30px}
.stars{color:#f5a623;font-size:11px;letter-spacing:1px}
.quote p{font-size:11px;line-height:18px;color:var(--text);margin-top:12px}
.who{position:absolute;left:32px;bottom:28px;display:flex;align-items:center;gap:14px}
.avatar{width:38px;height:38px;border-radius:50%;background:linear-gradient(#c9ccd3,#7b7f88)}
.who b{display:block;font-size:11.5px;font-weight:600}
.who span{font-size:10px;color:var(--muted)}

/* contact */
.contact{top:3605px;height:485px;background:var(--band)}
.contact .label{position:absolute;left:158px;top:128px}
.contact h2{position:absolute;left:156px;top:160px;font-size:46px;line-height:56px;font-weight:600;letter-spacing:-.5px}
.info{position:absolute;display:flex;gap:14px;font-size:10.5px;line-height:15px;color:var(--text)}
.ic{width:24px;height:24px;border-radius:50%;background:#fbe1d2;display:flex;align-items:center;justify-content:center;flex:none}
.field{position:absolute;border-bottom:1px solid var(--line);font-size:10.5px;color:var(--text);padding:0 0 14px 12px}
.consent{position:absolute;left:622px;top:345px;display:flex;gap:10px;align-items:center;font-size:8px;color:var(--muted)}
.consent i{width:14px;height:14px;border:1px solid #b5b8be;display:block}
.contact .btn{left:883px;top:337px;width:160px;height:42px}

/* blog */
.blog{top:4090px;height:640px}
.blog .label{position:absolute;left:0;width:1200px;text-align:center;top:106px}
.blog .sec-title{top:140px}
.post{position:absolute;top:228px;width:282px}
.post .ph{height:192px}
.post time{display:block;font-size:8px;color:var(--text);margin-top:20px}
.post h4{font-size:15px;font-weight:500;line-height:24px;margin-top:14px}
.post a{display:block;color:var(--orange);font-size:11.5px;font-weight:600;text-decoration:none;margin-top:14px}

/* footer */
.site-footer{top:4730px;height:355px;background:var(--band)}
.site-footer .brand{left:158px;top:112px}
.connect{position:absolute;left:156px;top:178px;font-size:10px}
.socials{position:absolute;left:156px;top:196px;display:flex;gap:7px}
.socials i{width:21px;height:21px;border:1.5px solid var(--ink);border-radius:50%;display:block}
.copy{position:absolute;left:156px;top:248px;font-size:8.5px;color:var(--text)}
.divider{position:absolute;left:459px;top:108px;width:1px;height:76px;background:var(--ink)}
.fcol{position:absolute;top:104px;font-size:10px;color:var(--text)}
.fcol h5{font-size:14px;font-weight:500;color:var(--ink);margin-bottom:22px}
.fcol li{list-style:none;height:32px}
</style>
</head>
<body>

<header class="site-header">
  <div class="brand"><i></i>Quillomette Morlewy</div>
  <nav class="nav"><span>Our services</span><span>About</span><span>Downloads</span><span>Contact Us</span><span>Links</span><span>◍ EN ⌄</span></nav>
  <div class="btn phone-btn">✆ (+612) 9000 4512</div>
</header>

<section class="hero">
  <div class="hero-photo" role="img" aria-label="Sydney harbour at dusk with the harbour bridge and opera house"></div>
  <div class="hero-card">
    <h1>The Goal Is To Provide<br><strong>Proffessional Service</strong></h1>
    <p>We are a firm of French-speaking lawyers located in the Sydney</p>
    <div class="btn">Request a Free Consultation</div>
  </div>
</section>

<section class="trust">
  <h2>Experience You Can Trust</h2>
  <p>Sed ut perspiciatis unde omnis iste natus error sit voluptatem accusantium doloremque laudantium, totam rem aperiam, eaque ipsa quae ab illo inventore veritatis et quasi architecto beatae vitae dicta sunt explicabo. Nemo enim ipsam voluptatem quia voluptas sit aspernatur aut odit aut.</p>
  <div class="win"><span>Pay Nothing Unless</span><strong>We Win</strong></div>
</section>

<section class="reasons">
  <h2 class="sec-title">Reasons to Choose Us</h2>
  <div class="reason" style="left:156px">
    <svg width="42" height="42" viewBox="0 0 42 42" fill="none" stroke-width="2"><rect x="6" y="8" width="18" height="26" rx="3" stroke="#1d1d1f"/><circle cx="29" cy="14" r="9" stroke="#f46a1f"/><text x="25" y="18" font-size="10" fill="#f46a1f" stroke="none">%</text></svg>
    <h3>Low Contingency Rate</h3>
    <p>Nam libero tempore, cum soluta nobis est eligendi optio cumque nihil impedit quo minus.</p>
    <svg class="go" width="22" height="10"><path d="M1 5h19M15 1l5 4-5 4" stroke="#f46a1f" fill="none" stroke-width="1.5"/></svg>
  </div>
  <div class="reason" style="left:460px">
    <svg width="42" height="42" viewBox="0 0 42 42" fill="none" stroke-width="2"><path d="M20 6l12 12-5 5-12-12z" stroke="#1d1d1f"/><path d="M18 20L6 32" stroke="#1d1d1f"/><rect x="10" y="32" width="22" height="5" stroke="#f46a1f"/></svg>
    <h3>Experienced Attorneys</h3>
    <p>At vero eos et accusamus et iusto odio dignissimos ducimus qui blanditiis praesentium</p>
    <svg class="go" width="22" height="10"><path d="M1 5h19M15 1l5 4-5 4" stroke="#f46a1f" fill="none" stroke-width="1.5"/></svg>
  </div>
  <div class="reason" style="left:764px">
    <svg width="42" height="42" viewBox="0 0 42 42" fill="none" stroke-width="2"><circle cx="14" cy="24" r="10" stroke="#f46a1f"/><text x="10" y="29" font-size="12" fill="#f46a1f" stroke="none">?</text><rect x="22" y="6" width="16" height="12" rx="3" stroke="#1d1d1f"/></svg>
    <h3>Free Consultation</h3>
    <p>Et harum quidem rerum facilis est et expedita distinctio. Nam libero tempore, cum soluta nobis est</p>
    <svg class="go" width="22" height="10"><path d="M1 5h19M15 1l5 4-5 4" stroke="#f46a1f" fill="none" stroke-width="1.5"/></svg>
  </div>
</section>

<section class="serve">
  <div class="serve-photo" role="img" aria-label="Three attorneys in business attire standing in front of a grey wall"></div>
  <div class="serve-panel">
    <h2>We Serve All of Sydney,<br>We Come to You</h2>
    <p>Trust the results. Our team of legal experts and attorneys can get you the compensation you seek and the results you require.</p>
    <div class="btn">Do I Have A Case?</div>
  </div>
</section>

<section class="awards">
  <h2 class="sec-title">Award-Winning Attorneys</h2>
  <svg class="abs" style="left:108px;top:226px" width="12" height="20"><path d="M10 2L3 10l7 8" stroke="#1d1d1f" fill="none" stroke-width="1.6"/></svg>
  <div class="badge" style="left:164px;background:#fff;border-color:#9fd3b5"></div>
  <div class="badge" style="left:308px"></div>
  <div class="badge" style="left:448px;background:#b9c6e4;border-color:#8aa0cf"></div>
  <div class="badge sq" style="left:598px;background:#2b3a78;border-color:#2b3a78"></div>
  <div class="badge" style="left:706px;background:#eef2f8;border-color:#3b5c9a"></div>
  <div class="badge" style="left:838px;background:#2f4b96;border-color:#d9a72a"></div>
  <div class="badge" style="left:956px;background:#1f4b9c;border-color:#1f4b9c"></div>
  <svg class="abs" style="left:1080px;top:226px" width="12" height="20"><path d="M2 2l7 8-7 8" stroke="#f46a1f" fill="none" stroke-width="1.6"/></svg>
  <div class="dots" style="left:564px;top:332px"><i></i><i></i><i></i><i></i></div>
</section>

<section class="cases">
  <div class="label">Cases We Handle</div>
  <h2>A Wide Range Of Legal Services To Solve Any Legal Issues</h2>
  <p class="intro">There are many variations of passages of Lorem Ipsum available, but the majority have suffered alteration in some form, by injected humour, or randomised words which don't look even slightly believable. If you are going to use a passage of Lorem Ipsum, you need to be sure there isn't anything embarrassing hidden in the middle of text. All the Lorem Ipsum generators on the Internet tend.</p>
  <div class="case active" style="left:156px"><div class="ph" role="img" aria-label="Modern apartment buildings" style="background:linear-gradient(#e9ebee,#7d828a);outline:2px solid var(--orange)"></div><h4>Property Law</h4></div>
  <div class="case" style="left:384px"><div class="ph" role="img" aria-label="Scales of justice on a desk in warm light" style="background:linear-gradient(135deg,#2a1e16,#8a6440 60%,#1d1510)"></div><h4>Sale of Business</h4></div>
  <div class="case" style="left:612px"><div class="ph" role="img" aria-label="Lawyers meeting at a table" style="background:linear-gradient(#a9b4c4,#dfe3e8)"></div><h4>Wills &amp; Estates</h4></div>
  <div class="case" style="left:840px"><div class="ph" role="img" aria-label="Interpreter with a headset at a laptop" style="background:linear-gradient(#f1f1f1,#d8d4cf)"></div><h4>Translation</h4></div>
  <div class="case" style="left:1068px"><div class="ph" role="img" aria-label="Bronze scales of justice" style="background:linear-gradient(135deg,#e4e4e4,#8b7a66)"></div><h4>Elder Law</h4></div>
  <div class="track"><i></i></div>
  <div class="arrow-btn off" style="left:958px;top:673px"><svg width="8" height="12"><path d="M6 1L1 6l5 5" stroke="#9a9da4" fill="none" stroke-width="1.5"/></svg></div>
  <div class="arrow-btn on" style="left:1007px;top:671px;width:34px;height:34px"><svg width="8" height="12"><path d="M2 1l5 5-5 5" stroke="#fff" fill="none" stroke-width="1.5"/></svg></div>
</section>

<section class="testimonials">
  <h2 class="sec-title">See What Our Clients<br>Are saying</h2>
  <div class="arrow-btn off" style="left:90px;top:352px"><svg width="8" height="12"><path d="M6 1L1 6l5 5" stroke="#1d1d1f" fill="none" stroke-width="1.5"/></svg></div>
  <div class="quote" style="left:156px"><div class="qmark">“</div><div class="stars">★★★★★</div>
    <p>Awesome attorney! I had a great experience with Mona. From day one, she was very clear in explaining the process. Every step of the way, she was very professional &amp; friendly.</p>
    <div class="who"><div class="avatar" role="img" aria-label="Client portrait"></div><div><b>Fred</b><span>Elk Avenue</span></div></div></div>
  <div class="quote" style="left:460px"><div class="qmark">“</div><div class="stars">★★★★★</div>
    <p>Great legal services. I am pleased to have chosen Mona as my attorney to handle my legal issues. Her staff and expertise made a great difference in the outcome.</p>
    <div class="who"><div class="avatar" role="img" aria-label="Client portrait"></div><div><b>Alejandra</b><span>Corpus Christi</span></div></div></div>
  <div class="quote" style="left:764px"><div class="qmark">“</div><div class="stars">★★★★★</div>
    <p>Super helpful staff. Not only did they include personal pain and suffering in my case but also managed to consider the sick hours I had to use for treatment.</p>
    <div class="who"><div class="avatar" role="img" aria-label="Client portrait"></div><div><b>Israel</b><span>College View</span></div></div></div>
  <div class="arrow-btn on" style="left:1078px;top:352px"><svg width="8" height="12"><path d="M2 1l5 5-5 5" stroke="#fff" fill="none" stroke-width="1.5"/></svg></div>
  <div class="dots" style="left:564px;top:532px"><i></i><i></i><i></i><i></i></div>
</section>

<section class="contact">
  <div class="label">Contact Us</div>
  <h2>Stay In The<br>Know</h2>
  <div class="info" style="left:156px;top:305px;align-items:center"><div class="ic"><svg width="11" height="11" viewBox="0 0 12 12"><path d="M2 1l3 1 1 3-2 1q1 2 3 3l1-2 3 1 0 3Q4 11 1 2z" fill="#f46a1f"/></svg></div>(+612) 9000 4512</div>
  <div class="info" style="left:314px;top:305px"><div class="ic"><svg width="10" height="12" viewBox="0 0 10 12"><path d="M5 11S1 7 1 4.5a4 4 0 018 0C9 7 5 11 5 11z" fill="#f46a1f"/></svg></div><span>Level 8, 42 Harbour Lane<br>Sydney, NSW 2000<br>Australia</span></div>
  <div class="info" style="left:156px;top:358px;align-items:center"><div class="ic"><svg width="11" height="9"><rect x=".5" y=".5" width="10" height="8" fill="#f46a1f"/></svg></div>hello@morlewy.com.au</div>
  <div class="field" style="left:626px;top:127px;width:204px">First Name*</div>
  <div class="field" style="left:842px;top:127px;width:200px">Last Name*</div>
  <div class="field" style="left:626px;top:193px;width:204px">Email Address*</div>
  <div class="field" style="left:842px;top:193px;width:200px">Zip Code</div>
  <div class="field" style="left:626px;top:273px;width:416px">Type Your Message</div>
  <div class="consent"><i></i>I have read and agree to the Privacy Policy</div>
  <div class="btn">Submit Request</div>
</section>

<section class="blog">
  <div class="label">Trending Blogs</div>
  <h2 class="sec-title">Award-Winning Law Blog</h2>
  <div class="arrow-btn off" style="left:90px;top:306px"><svg width="8" height="12"><path d="M6 1L1 6l5 5" stroke="#1d1d1f" fill="none" stroke-width="1.5"/></svg></div>
  <div class="post" style="left:156px"><div class="ph" role="img" aria-label="Lawyer signing documents beside a gavel" style="background:linear-gradient(135deg,#c9cdd3,#5b5e66)"></div><time>July 12, 2023</time><h4>Sed ut perspiciatis unde omnis iste natus error sit voluptatem</h4><a>Read More ›</a></div>
  <div class="post" style="left:460px"><div class="ph" role="img" aria-label="Gavel on a table with a city in soft focus" style="background:linear-gradient(135deg,#dfe4ea,#7a5a3a 70%)"></div><time>July 12, 2023</time><h4>Quia consequuntur magni dolores eos qui ratione</h4><a>Read More ›</a></div>
  <div class="post" style="left:764px"><div class="ph" role="img" aria-label="Scales of justice and a gavel on a pale background" style="background:linear-gradient(135deg,#f0f0f0,#9a9a9a)"></div><time>July 12, 2023</time><h4>Ut enim ad minima veniam, quis nostrum exercitationem</h4><a>Read More ›</a></div>
  <div class="arrow-btn on" style="left:1078px;top:306px"><svg width="8" height="12"><path d="M2 1l5 5-5 5" stroke="#fff" fill="none" stroke-width="1.5"/></svg></div>
</section>

<footer class="site-footer">
  <div class="brand"><i></i>Quillomette Morlewy</div>
  <div class="connect">Connect With Us</div>
  <div class="socials"><i></i><i></i><i></i><i></i></div>
  <div class="copy">©2024 Quillomette Morlewy solicitors. All rights reserved.</div>
  <div class="divider"></div>
  <div class="fcol" style="left:550px"><h5>Quick Links</h5><ul><li>Our services</li><li>About</li><li>Testimonials</li><li>Results</li><li>Contact</li></ul></div>
  <div class="fcol" style="left:729px"><h5>Helpful Links</h5><ul><li>Blog</li><li>Resource Library</li><li>Lumen University</li><li>Support</li><li>Legal</li></ul></div>
  <div class="fcol" style="left:902px"><h5>Contact Us</h5><ul><li>Level 8, 42 Harbour</li><li>Lane Sydney, NSW 2000</li><li>Australia</li><li>(+612) 9000 4512</li><li>hello@morlewy.com.au</li></ul></div>
</footer>

</body>
</html>
```